Talvero Networks LLC
Consultant, Health Care Operations
Talvero Networks LLC -
Creative Brief
Use specific fonts
I like Calibri, Tahoma, Lucida (rounded but professional) but am open to other similar fonts
Simple
Dwight Pennock
President, CEO
PO BOX 418263 Maple Harbor, FL 34920
dwight@talverohub.com
talverohub.com

```html
<!DOCTYPE html>
<html lang="en">
<head>
<meta charset="utf-8">
<title>Talvero Networks LLC – Business Card</title>
<link href="https://fonts.googleapis.com/css2?family=Open+Sans:wght@400;600;700&display=swap" rel="stylesheet">
<style>
  :root {
    --bg: #e9eaec;
    --card: #ffffff;
    --blue: #2aa8e0;
    --navy: #1d2b3a;
    --ink: #1a1a1a;
  }
  * { margin: 0; padding: 0; box-sizing: border-box; }
  html, body { width: 1200px; height: 943px; overflow: hidden; }
  body {
    background: var(--bg);
    font-family: "Open Sans", Arial, sans-serif;
    position: relative;
  }
  .card {
    position: absolute;
    width: 598px;
    height: 339px;
    background: var(--card);
    border-radius: 22px;
    overflow: hidden;
    box-shadow: 0 4px 14px rgba(0,0,0,.18);
  }
  .card--front { left: 413px; top: 82px; }
  .card--back  { left: 99px;  top: 443px; }

  .card__swoosh { position: absolute; left: 0; top: 0; width: 598px; height: 339px; }

  .brand { position: absolute; display: flex; flex-direction: column; align-items: center; }
  .brand__dot { width: 44px; height: 44px; border-radius: 50%; background: var(--blue); margin-bottom: 12px; }
  .brand__name {
    color: var(--navy);
    font-weight: 700;
    font-size: 28px;
    line-height: 1.1;
    text-align: center;
    letter-spacing: .5px;
  }
  .card--front .brand { left: 30px; top: 40px; width: 230px; }
  .card--back .brand { left: 149px; top: 70px; width: 300px; }
  .card--back .brand__dot { width: 56px; height: 56px; }
  .card--back .brand__name { font-size: 38px; }

  .contact {
    position: absolute;
    right: 26px;
    top: 56px;
    text-align: right;
    color: var(--ink);
  }
  .contact__name { color: var(--blue); font-weight: 700; font-size: 22px; line-height: 1.2; }
  .contact__title { font-size: 17px; line-height: 1.3; margin-bottom: 34px; }
  .contact__line { font-size: 15px; line-height: 24px; }
  .contact__label { color: var(--blue); font-weight: 700; }

  .card__url {
    position: absolute;
    font-size: 15px;
    letter-spacing: 1.5px;
  }
  .card--front .card__url { left: 22px; bottom: 8px; color: #ffffff; }
  .card--back .card__url { left: 0; right: 0; bottom: 28px; text-align: center; color: var(--blue); }
</style>
</head>
<body>

  <section class="card card--front">
    <svg class="card__swoosh" viewBox="0 0 598 339" aria-hidden="true">
      <path d="M0 252 C 200 322, 420 272, 598 244 L598 339 L0 339 Z" fill="var(--blue)"/>
      <path d="M0 266 C 200 324, 420 288, 598 262" fill="none" stroke="#ffffff" stroke-width="5"/>
      <path d="M230 314 C 380 292, 490 266, 598 238" fill="none" stroke="#111" stroke-width="3"/>
    </svg>

    <div class="brand">
      <span class="brand__dot"></span>
      <span class="brand__name">Talvero Networks LLC</span>
    </div>

    <div class="contact">
      <p class="contact__name">Dwight Pennock</p>
      <p class="contact__title">President, CEO</p>
      <p class="contact__line">PO BOX 418263</p>
      <p class="contact__line">Maple Harbor, FL 34920</p>
      <p class="contact__line"><span class="contact__label">P :</span> 321.555.0192</p>
      <p class="contact__line"><span class="contact__label">E :</span> dwight@talverohub.com</p>
    </div>

    <p class="card__url">www.talverohub.com</p>
  </section>

  <section class="card card--back">
    <div class="brand">
      <span class="brand__dot"></span>
      <span class="brand__name">Talvero Networks LLC</span>
    </div>
    <p class="card__url">www.talverohub.com</p>
  </section>

</body>
</html>
```